Flyer for Compassion training days

I need a A5-size, single-sided flyer design for my training days. They are weekends in a blend of Compassionate Communication and Buddhist teachings called Palomere Communication. The logo for Palomere that should be included.
The flyer needs room for 1) course title, 2) course dates, location & price, 3) course description, 4) booking info, 5) my picture & short bio, and 6) the palomere.co website (yes, it is 'co' and not 'com).
Updates

Target Market(s)

Women 35-65 years, well-educated, spiritually minded. May have interests like yoga and meditation.

Industry/Entity Type

Health And Wellness

Font styles to use
Sans Serif
Other font styles liked:
• Blue Plaque, Josefina are both great

Colors
fbf289
fdf9cf
cfeae6
33b8a4

Requirements
Must have
• The Palomere logo; my picture.
• Elegance. Calm and expansive feel.
• The poster provided in the project files shows you the kind of information I need to include.
• Colours -- greens and yellows, but the options on pixel harbor are not quite the right shades.
• The logo colour can be changed.
Nice to have
• Classy (but not cliche) image associated with Buddhism; gentle curves similar to those on the business card (see project files).
Should not have
• Dark background. Busy, loud design. Overly 'swirly' design. Images that I have to buy separately.

```html
<!DOCTYPE html>
<html lang="en">
<head>
<meta charset="utf-8">
<title>Palomere Communication Core Course – Flyer</title>
<link rel="stylesheet" href="https://fonts.googleapis.com/css2?family=Josefin+Sans:ital,wght@0,300;0,400;0,600;0,700;1,400&family=Arimo&display=swap">
<style>
  :root {
    --backdrop: #0f1411;
    --cream: #fdf9cf;
    --sky: #eef3ef;
    --yellow: #fbf289;
    --mint: #cfeae6;
    --green: #3fae3c;
    --green-light: #8cc84b;
    --green-dark: #1f9a3a;
    --title-red: #8f3a35;
    --text-red: #9b2a33;
    --text-brown: #5c3a30;
    --contact-red: #8a1c2a;
    --white: #ffffff;
  }
  * { margin: 0; padding: 0; box-sizing: border-box; }
  html, body { width: 1200px; height: 1200px; overflow: hidden; background: var(--backdrop); }
  body { position: relative; font-family: "Josefin Sans", sans-serif; }

  .flyer {
    position: absolute; left: 269px; top: 123px; width: 664px; height: 931px;
    background: var(--cream); overflow: hidden;
  }
  .flyer > * { position: absolute; }

  .hero-landscape {
    left: 0; top: 0; width: 664px; height: 293px;
    background: linear-gradient(180deg, #f3f6f4 0%, #e4ebe6 45%, #c9d2b8 75%, #e7e3cf 100%);
  }
  .hero-statue {
    left: 343px; top: 57px; width: 200px; height: 236px;
    background: radial-gradient(ellipse at 50% 55%, #c9a04a 0%, #a87f2c 55%, rgba(168,127,44,0) 75%);
  }
  .brand-mark {
    display: flex; align-items: center; gap: 8px;
    font-weight: 600; color: var(--green); font-size: 22px;
  }
  .brand-mark .dot { width: 14px; height: 14px; border-radius: 50%; background: var(--green); }
  .brand-top { left: 488px; top: 100px; }
  .brand-bottom { left: 490px; top: 600px; }

  .tagline {
    left: 42px; top: 47px; font-size: 19px; font-weight: 300; line-height: 23px; color: var(--text-brown);
  }
  .tagline .plus { color: var(--green); }
  .course-title {
    left: 42px; top: 99px; font-size: 27px; font-weight: 600; line-height: 29px; color: var(--title-red);
    text-transform: uppercase; letter-spacing: 0.3px;
  }
  .course-title span { display: block; }

  .event-box {
    left: 0; top: 225px; width: 289px; height: 68px; background: var(--yellow);
    padding: 4px 0 0 42px; color: var(--text-brown); line-height: 20px;
  }
  .event-date { font-size: 21px; font-weight: 600; }
  .event-venue { font-size: 18px; font-weight: 400; }
  .event-price { font-size: 17px; font-weight: 600; color: var(--green-dark); }

  .intro {
    left: 42px; top: 306px; width: 580px; font-size: 15.5px; font-weight: 300; line-height: 19.5px; color: var(--text-brown);
  }
  .flower-art {
    left: 378px; top: 353px; width: 83px; height: 68px;
    background: radial-gradient(ellipse at 35% 45%, #eea5b1 0%, #d9a5a8 40%, rgba(180,200,170,0.4) 70%, rgba(0,0,0,0) 80%);
  }
  .explore-heading {
    left: 42px; top: 379px; font-size: 18px; font-weight: 600; color: var(--text-brown);
  }
  .topic-list { left: 42px; top: 409px; list-style: none; }
  .topic-list li {
    display: flex; align-items: center; gap: 6px; height: 20px;
    font-size: 16px; color: var(--text-red);
  }
  .topic-list svg { width: 18px; height: 16px; flex: none; }

  .audience {
    left: 42px; top: 498px; width: 580px; font-size: 15.5px; font-style: italic; line-height: 19.5px; color: var(--text-brown);
  }
  .booking { left: 42px; top: 578px; color: var(--text-red); }
  .booking-line { font-size: 19px; font-weight: 300; }
  .booking-line strong { font-weight: 700; font-style: italic; }
  .booking-email { font-size: 24px; font-weight: 600; color: var(--contact-red); margin-top: 1px; }

  .wave { left: 0; top: 620px; width: 664px; height: 222px; }

  .facilitator-photo {
    left: 42px; top: 678px; width: 121px; height: 146px;
    border: 3px solid var(--white);
    background: linear-gradient(160deg, #c8a878 0%, #9c7a52 60%, #6e5235 100%);
  }
  .bio {
    left: 174px; top: 702px; width: 450px; font-size: 16px; line-height: 19px; color: var(--white); font-weight: 400;
  }
  .coaching {
    left: 174px; top: 776px; font-size: 17px; line-height: 19px; color: var(--white); font-weight: 300; text-transform: uppercase;
  }
  .coaching strong { font-weight: 600; }
  .website {
    left: 440px; top: 805px; display: flex; align-items: center; gap: 5px;
    font-size: 20px; font-weight: 600; color: var(--white);
  }
  .website svg { width: 18px; height: 18px; }

  .contact-strip {
    left: 0; top: 841px; width: 664px; height: 90px; background: var(--mint);
  }
  .contact-list {
    left: 42px; top: 860px; display: flex; gap: 20px;
    font-family: "Arimo", sans-serif; font-size: 20px; color: var(--contact-red);
  }
  .contact-list span { display: flex; align-items: center; gap: 4px; }
  .contact-list svg { width: 16px; height: 18px; }
</style>
</head>
<body>
<main class="flyer">
  <div class="hero-landscape" role="img" aria-label="Misty hillside landscape with trees"></div>
  <div class="hero-statue" role="img" aria-label="Golden seated Buddha statue resting its head on its knees"></div>
  <div class="brand-mark brand-top"><span class="dot"></span>Palomere</div>

  <p class="tagline">Mindfulness <span class="plus">+</span> Kindness <span class="plus">+</span><br>Compassionate Communication =</p>
  <h1 class="course-title"><span>Palomere</span><span>Communication</span><span>Core</span><span>Course</span></h1>

  <div class="event-box">
    <div class="event-date">11-12 Dec</div>
    <div class="event-venue">Rowanbank Centre, Edinburgh</div>
    <div class="event-price">(£125/100)</div>
  </div>

  <p class="intro">Palomere Communication can help you increase awareness &amp; compassion in every-day speech (with yourself &amp; others), better understand your own patterns, and build resilience to challenging situations. Choose from:</p>
  <div class="flower-art" role="img" aria-label="Watercolour pink peony flowers"></div>

  <h2 class="explore-heading">In this 2-day Core Course, we’ll explore:</h2>
  <ul class="topic-list">
    <li><svg viewBox="0 0 18 16"><path d="M1 9 L6 14 L17 2" fill="none" stroke="#3fae3c" stroke-width="3.5" stroke-linecap="round"/></svg>Compassionate Communication;</li>
    <li><svg viewBox="0 0 18 16"><path d="M1 9 L6 14 L17 2" fill="none" stroke="#3fae3c" stroke-width="3.5" stroke-linecap="round"/></svg>Buddhist teachings on Right Speech, loving-kindness, Right Effort, and more;</li>
    <li><svg viewBox="0 0 18 16"><path d="M1 9 L6 14 L17 2" fill="none" stroke="#3fae3c" stroke-width="3.5" stroke-linecap="round"/></svg>Mindfulness practices;</li>
    <li><svg viewBox="0 0 18 16"><path d="M1 9 L6 14 L17 2" fill="none" stroke="#3fae3c" stroke-width="3.5" stroke-linecap="round"/></svg>Choices available to us in our everyday speech.</li>
  </ul>

  <p class="audience">This workshop will be of interest if you’d like to improve personal and/or profes-sional relationships. &nbsp;Open to all, best suited to those with at least 1 year’s experi-ence with Mindfulness, &nbsp;Buddhism, or Compassionate Communication / NVC.</p>

  <div class="booking">
    <p class="booking-line"><strong>BOOKING:</strong> Book online at TicketGrove or write</p>
    <p class="booking-email">marisol@palomere.co</p>
  </div>

  <svg class="wave" viewBox="0 0 664 222" preserveAspectRatio="none">
    <defs>
      <linearGradient id="bandFill" x1="0" y1="0" x2="0" y2="1">
        <stop offset="0" stop-color="#8cc84b"/>
        <stop offset="1" stop-color="#2fae3e"/>
      </linearGradient>
    </defs>
    <path d="M0 40 C160 15 300 30 420 55 C520 75 600 60 664 45 L664 222 L0 222 Z" fill="url(#bandFill)"/>
    <path d="M0 30 C150 8 320 14 470 40 C520 49 560 52 580 55 L568 62 L600 55 L572 46 C400 15 200 0 0 22 Z" fill="#2faa3b"/>
  </svg>

  <div class="brand-mark brand-bottom"><span class="dot"></span>Palomere</div>

  <div class="facilitator-photo" role="img" aria-label="Portrait photo of the facilitator"></div>
  <p class="bio">Facilitator: &nbsp;Marisol Avenhurst is an experienced group facilitator, having worked with a range of organisations and presented at a number of festivals &amp; conferences.</p>
  <p class="coaching">Marisol offers coaching in<br><strong>Palomere Communication.</strong></p>
  <p class="website"><svg viewBox="0 0 18 18"><g fill="none" stroke="#fff" stroke-width="1.3"><circle cx="9" cy="9" r="8"/><ellipse cx="9" cy="9" rx="3.5" ry="8"/><path d="M1 9 H17 M2.5 5 H15.5 M2.5 13 H15.5"/></g></svg>www.palomere.co</p>

  <div class="contact-strip"></div>
  <div class="contact-list">
    <span><svg viewBox="0 0 16 18"><path d="M5 2 C2 4 2 14 5 16 L7 13 C5.5 11 5.5 7 7 5 Z" fill="#3fae3c"/></svg>01632 960 555</span>
    <span><svg viewBox="0 0 16 18"><rect x="3" y="1" width="10" height="16" rx="1.5" fill="#3fae3c"/><rect x="5" y="3" width="6" height="5" fill="#cfeae6"/></svg>07700 900 434</span>
    <span><svg viewBox="0 0 22 18" style="width:22px"><rect x="1" y="3" width="20" height="13" fill="none" stroke="#3fae3c" stroke-width="1.4"/><path d="M1 3 L11 11 L21 3 M1 16 L8 9 M21 16 L14 9" fill="none" stroke="#3fae3c" stroke-width="1.4"/></svg>marisol@palomere.co</span>
  </div>
</main>
</body>
</html>
```